Ledge Crafts one page flyer

We need a standard A4 size flyer for a new company called Ledge Crafts. We are a construction material company and sell trims, crown mouldings, baseboards and panelings.
We would like to see the design with the following information:
1. Size: A4
2. Only one front page, no design need to display on back
3. Logo (Ledge Crafts, see the attached EPS file)
4. Slogan: We offer high quality products for competitive prices.
5. Content please see the PDF file
6. The production has 2 category, one called "Crown Moulding", the other is "Wainscoting", Crown Moulding has 5 productions, wainscoting has 2 production(Details see PDF file)
6. We temporary only can provide low resolution images for 7 productions, only the winner will be provided with High Resolution images.
Look and feel
Each slider illustrates characteristics of the customer's brand and the style your logo design should communicate.

```html
<!DOCTYPE html>
<html lang="en">
<head>
<meta charset="utf-8">
<title>Ledge Crafts Flyer</title>
<link href="https://fonts.googleapis.com/css2?family=Bebas+Neue&family=Montserrat:wght@500;600;700&family=Lato:wght@300;400&display=swap" rel="stylesheet">
<style>
:root{
  --blue:#4a90d9;
  --orange:#f0522a;
  --black:#111;
  --grey:#5d6670;
  --white:#fff;
}
*{margin:0;padding:0;box-sizing:border-box}
html,body{width:869px;height:1200px;overflow:hidden;background:var(--white)}
.flyer{position:relative;width:869px;height:1200px;font-family:'Montserrat',sans-serif;color:var(--black)}
.abs{position:absolute}
.brand{left:22px;top:34px;display:flex;align-items:center;gap:14px}
.brand-mark{width:40px;height:40px;background:var(--blue)}
.brand-name{font-family:'Lato',sans-serif;font-weight:300;font-size:40px;letter-spacing:3px;color:var(--grey);line-height:1}
.brand-tag{left:103px;top:82px;font-family:'Lato',sans-serif;font-weight:300;font-size:13px;letter-spacing:3px;color:var(--grey)}
.call{left:452px;top:0;width:417px;height:120px;background:var(--blue);clip-path:polygon(25px 0,100% 0,100% 100%,0 100%)}
.call-icon{left:488px;top:32px}
.call-title{left:578px;top:14px;font-family:'Bebas Neue',sans-serif;font-size:64px;color:var(--white);line-height:1;letter-spacing:1px}
.call-phone{left:580px;top:74px;font-family:'Montserrat',sans-serif;font-weight:500;font-size:35px;color:var(--white);line-height:1}
.photo{left:0;top:120px;width:869px;height:421px;background:linear-gradient(135deg,#3d4240 0%,#5b5f5a 40%,#b38558 50%,#5a5e5a 62%,#2e3230 100%)}
.slogan{left:0;top:541px;width:869px;height:72px;background:var(--blue);display:flex;align-items:center;justify-content:center;font-family:'Bebas Neue',sans-serif;font-size:44px;color:var(--white);letter-spacing:.5px}
.slogan-tab{left:318px;top:611px;width:232px;height:10px;background:var(--blue);border-radius:0 0 10px 10px;border:2px solid var(--white);border-top:none}
.rule{left:0;top:666px;width:869px;border-top:2px dotted var(--black)}
.section-title{font-family:'Montserrat',sans-serif;font-weight:500;color:var(--white);background:var(--black);line-height:1}
.crown-title{left:262px;top:650px;width:346px;height:33px;font-size:27px;display:flex;align-items:center;justify-content:center;clip-path:polygon(10px 0,calc(100% - 10px) 0,100% 50%,calc(100% - 10px) 100%,10px 100%,0 50%)}
.wains-title{left:0;top:886px;width:244px;height:32px;font-size:27px;padding-left:20px;display:flex;align-items:center;clip-path:polygon(0 0,calc(100% - 12px) 0,100% 50%,calc(100% - 12px) 100%,0 100%)}
.hours-title{left:610px;top:886px;width:259px;height:32px;font-size:27px;padding-left:28px;display:flex;align-items:center;clip-path:polygon(12px 0,100% 0,100% 100%,12px 100%,0 50%)}
.product{width:160px;height:140px}
.product svg{position:absolute;left:0;top:0}
.size{position:absolute;left:50%;top:6px;transform:translateX(-50%);background:var(--orange);color:var(--white);font-weight:500;font-size:13.5px;padding:5px 10px;border-radius:14px;white-space:nowrap}
.shot{position:absolute;left:40px;top:46px;width:80px;height:60px;background:linear-gradient(135deg,#1c1c1c 0%,#f2f2f2 55%,#d8d8d8 100%)}
.shot-empty{position:absolute;left:0;width:100%;top:68px;text-align:center;font-size:11px;font-weight:500}
.name{position:absolute;left:0;width:100%;bottom:8px;text-align:center;font-size:7.5px;font-weight:600;text-transform:uppercase}
.divider{left:476px;top:945px;height:130px;border-left:1px solid #e3e3e3}
.hours-icon{left:722px;top:936px}
.hours-line{right:22px;font-weight:700;font-size:23px;line-height:1}
.closed{color:var(--orange)}
.contact-tab{left:336px;top:1072px;width:199px;height:32px;background:var(--blue);border-radius:14px 14px 0 0;color:var(--white);font-weight:500;font-size:21px;display:flex;align-items:center;justify-content:center}
.footer{left:0;top:1103px;width:869px;height:97px;background:linear-gradient(90deg,#000 0%,#2a2a2a 60%,#000 100%);border-top:3px solid var(--blue)}
.foot-col{color:var(--white);font-size:10px;font-weight:500;line-height:16px}
.foot-col h4{font-size:11px;font-weight:600;text-decoration:underline;margin-bottom:6px}
.appointment{left:580px;top:1103px;width:289px;height:97px;background:var(--blue);clip-path:polygon(30px 0,100% 0,100% 100%,30px 100%,0 50%);display:flex;align-items:center;justify-content:flex-end;padding-right:20px;font-family:'Bebas Neue',sans-serif;font-size:38px;color:var(--white)}
</style>
</head>
<body>
<div class="flyer">
  <header>
    <div class="abs brand"><span class="brand-mark"></span><span class="brand-name">LEDGE CRAFTS</span></div>
    <div class="abs brand-tag">FOR ALL TYPES OF PROJECTS</div>
    <div class="abs call"></div>
    <svg class="abs call-icon" width="70" height="62" viewBox="0 0 70 62">
      <path d="M12 6c4-3 8-2 10 2l5 10c1 3 0 5-3 7l-4 3c3 8 9 14 17 18l3-4c2-3 4-4 7-3l10 5c4 2 5 6 2 10l-4 4c-6 5-20 1-33-12S6 12 12 6z" fill="none" stroke="#fff" stroke-width="4"/>
      <path d="M38 14a14 14 0 0 1 14 14M40 4a24 24 0 0 1 24 24" fill="none" stroke="#fff" stroke-width="4" stroke-linecap="round"/>
    </svg>
    <div class="abs call-title">CALL US NOW</div>
    <div class="abs call-phone">905-555-0148</div>
  </header>

  <div class="abs photo" role="img" aria-label="Overhead photo of three people reviewing construction plans at an office table"></div>
  <div class="abs slogan">WE OFFER HIGH QUALITY PRODUCTS FOR COMPETITIVE PRICES</div>
  <div class="abs slogan-tab"></div>

  <div class="abs rule"></div>
  <div class="abs section-title crown-title">• CROWN MOULDING •</div>

  <div class="abs product" style="left:18px;top:712px">
    <svg width="160" height="140"><path d="M20 132A76 76 0 1 1 140 132" fill="none" stroke="var(--orange)" stroke-width="1.5"/><path d="M130 34l4 6 3-8z" fill="var(--orange)"/></svg>
    <div class="size">8 7/16"X3/4"</div>
    <div class="shot" role="img" aria-label="Harbor 9 crown moulding profile"></div>
    <div class="name">Harbor 9 Crown Moulding</div>
  </div>
  <div class="abs product" style="left:186px;top:712px">
    <svg width="160" height="140"><path d="M20 132A76 76 0 1 1 140 132" fill="none" stroke="var(--orange)" stroke-width="1.5"/><path d="M130 34l4 6 3-8z" fill="var(--orange)"/></svg>
    <div class="size">7 3/4"X3/4"</div>
    <div class="shot" role="img" aria-label="Harbor 8 crown moulding profile"></div>
    <div class="name">Harbor 8 Crown Moulding</div>
  </div>
  <div class="abs product" style="left:355px;top:712px">
    <svg width="160" height="140"><path d="M20 132A76 76 0 1 1 140 132" fill="none" stroke="var(--orange)" stroke-width="1.5"/><path d="M130 34l4 6 3-8z" fill="var(--orange)"/></svg>
    <div class="size">6 1/2"X3/4"</div>
    <div class="shot" role="img" aria-label="Harbor 7 crown moulding profile"></div>
    <div class="name">Harbor 7 Crown Moulding</div>
  </div>
  <div class="abs product" style="left:524px;top:712px">
    <svg width="160" height="140"><path d="M20 132A76 76 0 1 1 140 132" fill="none" stroke="var(--orange)" stroke-width="1.5"/><path d="M130 34l4 6 3-8z" fill="var(--orange)"/></svg>
    <div class="size">7 3/4"X3/4"</div>
    <div class="shot" role="img" aria-label="Summit 8 crown moulding profile"></div>
    <div class="name">Summit 8 Crown Moulding</div>
  </div>
  <div class="abs product" style="left:691px;top:712px">
    <svg width="160" height="140"><path d="M20 132A76 76 0 1 1 140 132" fill="none" stroke="var(--orange)" stroke-width="1.5"/><path d="M130 34l4 6 3-8z" fill="var(--orange)"/></svg>
    <div class="size">6 1/4"X3/4"</div>
    <div class="shot" role="img" aria-label="Summit 6 crown moulding profile"></div>
    <div class="name">Summit 6 Crown Moulding</div>
  </div>

  <div class="abs section-title wains-title">WAINSCOTING</div>
  <div class="abs product" style="left:18px;top:938px">
    <svg width="160" height="140"><path d="M20 132A76 76 0 1 1 140 132" fill="none" stroke="var(--orange)" stroke-width="1.5"/><path d="M130 34l4 6 3-8z" fill="var(--orange)"/></svg>
    <div class="size">3 1/4"X1"</div>
    <div class="shot-empty">IMAGE</div>
    <div class="name">Colonial Chair Rail</div>
  </div>
  <div class="abs product" style="left:186px;top:938px">
    <svg width="160" height="140"><path d="M20 132A76 76 0 1 1 140 132" fill="none" stroke="var(--orange)" stroke-width="1.5"/><path d="M130 34l4 6 3-8z" fill="var(--orange)"/></svg>
    <div class="size">1 3/4"X5/8"</div>
    <div class="shot-empty">IMAGE</div>
    <div class="name">Colonial Panel Mould</div>
  </div>

  <div class="abs divider"></div>
  <div class="abs section-title hours-title">OFFICE HOURS</div>
  <svg class="abs hours-icon" width="46" height="44" viewBox="0 0 46 44">
    <rect x="2" y="6" width="32" height="30" rx="2" fill="none" stroke="var(--orange)" stroke-width="3"/>
    <path d="M2 14h32M10 2v8M26 2v8" stroke="var(--orange)" stroke-width="3"/>
    <path d="M8 19h5v4H8zM16 19h5v4h-5zM24 19h5v4h-5zM8 26h5v4H8zM16 26h5v4h-5z" fill="var(--orange)"/>
    <circle cx="34" cy="32" r="10" fill="#fff" stroke="var(--orange)" stroke-width="3"/>
    <path d="M34 26v6h5" fill="none" stroke="var(--orange)" stroke-width="2.5"/>
  </svg>
  <div class="abs hours-line" style="top:992px">MON – FRI : 7:00AM – 6:00PM</div>
  <div class="abs hours-line" style="top:1026px">SATURDAYS : 8:00AM – 4:00PM</div>
  <div class="abs hours-line closed" style="top:1060px">SUNDAYS : Closed</div>

  <div class="abs contact-tab">CONTACT US</div>
  <footer class="abs footer"></footer>
  <div class="abs foot-col" style="left:59px;top:1112px">
    <h4>LEDGE CRAFTS</h4>
    <div>● 412 Fieldstone Ave, unit 4, Maple Ridge, Ontario L4B 0A1</div>
    <div>✉ info@ledgecrafts.ca</div>
  </div>
  <div class="abs foot-col" style="left:380px;top:1112px">
    <h4>WAREHOUSE</h4>
    <div>● 78 Kestrel Dr, North York,</div>
    <div>&nbsp;&nbsp;&nbsp;ON M3J 0B2</div>
  </div>
  <div class="abs appointment">BY APPOINTMENT ONLY</div>
</div>
</body>
</html>
```